Pelin Thai Massage Double Sided Flyer Luxury

I require a double sided flyer
we are a Thai Massage Spa
Would like gold, deep purple and bronze colours
Something eye catching and looks professional

```html
<!DOCTYPE html>
<html lang="en">
<head>
<meta charset="utf-8">
<title>Pelin Thai Massage – Double Sided Flyer</title>
<link rel="stylesheet" href="https://fonts.googleapis.com/css2?family=Philosopher:wght@400;700&display=swap">
<style>
  :root {
    --stage: #6a6b6f;
    --cocoa: #2b140c;
    --cocoa-deep: #1c0c06;
    --cocoa-strip: #160904;
    --gold-light: #fbd35a;
    --gold: #f2b533;
    --gold-deep: #e69c17;
    --ink: #2a1709;
    --cream: #fbf3e4;
    --frame: #f4efe6;
  }
  * { box-sizing: border-box; margin: 0; padding: 0; }
  html, body { width: 1200px; height: 821px; overflow: hidden; }
  body {
    background: var(--stage);
    font-family: "Philosopher", sans-serif;
    position: relative;
  }
  .flyer {
    position: absolute;
    top: 88px;
    width: 498px;
    height: 644px;
    background: radial-gradient(ellipse at 50% 30%, #3a1c10 0%, var(--cocoa) 55%, var(--cocoa-deep) 100%);
    overflow: hidden;
  }
  .flyer--front { left: 88px; }
  .flyer--back { left: 614px; }

  .brand {
    position: absolute;
    top: 40px; left: 0; width: 100%;
    text-align: center;
  }
  .brand__circle {
    width: 100px; height: 100px;
    margin: 0 auto;
    border-radius: 50%;
    border: 3px solid var(--gold);
  }
  .brand__name {
    margin-top: 12px;
    font-size: 23px;
    color: var(--gold);
    letter-spacing: 0.3px;
  }

  .gold-band {
    position: absolute;
    left: 0; width: 100%;
    background: linear-gradient(90deg, var(--gold-deep) 0%, var(--gold-light) 50%, var(--gold-deep) 100%);
    color: var(--ink);
    text-align: center;
  }
  .gold-band--welcome { top: 190px; height: 108px; padding-top: 10px; }
  .gold-band--intro { top: 190px; height: 82px; padding-top: 12px; }
  .gold-band__title { font-size: 15px; margin-bottom: 6px; }
  .gold-band__text { font-size: 9.2px; line-height: 1.4; padding: 0 34px; }
  .gold-band__text + .gold-band__text { margin-top: 12px; }
  .gold-band__lead { font-size: 13px; line-height: 1.25; padding: 0 40px; margin-top: 6px; }

  .strip {
    position: absolute; left: 0; width: 100%;
    background: var(--cocoa-strip);
  }

  .photo {
    position: absolute;
    border: 2px solid var(--frame);
  }
  .photo--hero {
    top: 312px; left: 0; width: 498px; height: 158px;
    border: none;
    background: linear-gradient(100deg, #f1ece6 0%, #c98a5c 30%, #a0603a 60%, #b8895a 85%, #6d3d22 100%);
  }
  .photo-pair {
    position: absolute; left: 24px; width: 451px; height: 96px;
  }
  .photo-pair .photo { top: 0; height: 96px; }
  .photo-pair .photo--left {
    left: 0; width: 221px;
    clip-path: polygon(0 0, 100% 0, 93% 100%, 0 100%);
  }
  .photo-pair .photo--right {
    left: 206px; width: 245px;
    clip-path: polygon(6% 0, 100% 0, 100% 100%, 0 100%);
  }
  .tone-warm { background: linear-gradient(110deg, #5a2e16 0%, #b5784e 45%, #e8d6c4 100%); }
  .tone-lilac { background: linear-gradient(110deg, #8d5fb8 0%, #d7a35a 45%, #9a3f9a 100%); }
  .tone-face { background: linear-gradient(110deg, #f0ebe5 0%, #d9a47e 50%, #6f8f6f 100%); }
  .tone-back { background: linear-gradient(110deg, #7a4a2a 0%, #c98a5c 50%, #efe8e0 100%); }
  .tone-skin { background: linear-gradient(110deg, #f3eee9 0%, #e2bfa3 55%, #f7f3ef 100%); }

  .contact {
    position: absolute; left: 0; width: 100%;
    top: 588px;
    text-align: center;
    color: var(--cream);
    font-size: 16px;
    line-height: 20px;
  }

  .menu-title {
    position: absolute; top: 282px; left: 0; width: 100%;
    text-align: center;
    color: var(--gold);
    font-size: 24px;
  }
  .menu-bracket {
    position: absolute; top: 294px; left: 45px;
  }
  .price-card {
    position: absolute; top: 322px; width: 147px; height: 131px;
    background: linear-gradient(135deg, var(--gold-light) 0%, var(--gold) 55%, var(--gold-deep) 100%);
    color: var(--ink);
    text-align: center;
    padding-top: 11px;
  }
  .price-card--one { left: 19px; }
  .price-card--two { left: 176px; }
  .price-card--three { left: 332px; }
  .price-card__name { font-size: 10px; line-height: 1.2; height: 26px; text-transform: uppercase; }
  .price-card__rule { width: 100px; height: 1px; background: var(--ink); margin: 2px auto 0; }
  .price-card__time { font-size: 18px; margin-top: 5px; line-height: 1.1; }
  .price-card__price { font-size: 18px; line-height: 1.15; margin-bottom: 4px; }
  .price-card__note { font-size: 7px; line-height: 1.3; margin-top: 8px; padding: 0 8px; }
</style>
</head>
<body>

<section class="flyer flyer--front">
  <div class="brand">
    <div class="brand__circle"></div>
    <div class="brand__name">Pelin Thai Massage</div>
  </div>

  <div class="gold-band gold-band--welcome">
    <h2 class="gold-band__title">Welcome to Luxury</h2>
    <p class="gold-band__text">Set in the heart of Roundhay, Pelin Thai Massage will allow you to immerse yourself in a place where your wellbeing and rejuvenation is at the centre of what we do.</p>
    <p class="gold-band__text">Using Thai traditions, our highly trained therapists offer revitalising body treatments with their deep tissue massage techniques. In their hands, you will see and feel immediate results.</p>
  </div>
  <div class="strip" style="top:298px;height:14px"></div>

  <div class="photo photo--hero" role="img" aria-label="Woman with a flower in her hair receiving a back massage on a bamboo mat with candles"></div>

  <div class="photo-pair" style="top:483px">
    <div class="photo photo--left tone-warm" role="img" aria-label="Relaxed woman receiving a shoulder massage by candlelight"></div>
    <div class="photo photo--right tone-lilac" role="img" aria-label="Spa still life with candle, lavender salts and folded purple towel"></div>
  </div>

  <div class="contact">
    <p>42 Oak Row, Leeds, LS8 2BQ</p>
    <p>0113 496 0742 | www.pelinthaimassage.co.uk</p>
  </div>
</section>

<section class="flyer flyer--back">
  <div class="photo-pair" style="top:61px">
    <div class="photo photo--left tone-face" role="img" aria-label="Woman with a towel wrap enjoying a facial massage"></div>
    <div class="photo photo--right tone-back" role="img" aria-label="Woman with a flower in her hair receiving a back massage"></div>
  </div>

  <div class="gold-band gold-band--intro">
    <h2 class="gold-band__title">MASSAGES</h2>
    <p class="gold-band__lead">Restore balance. Revive your senses. Discover all the ways Pelin Thai Massage can breathe new life into your body and soul.</p>
  </div>
  <div class="strip" style="top:272px;height:8px"></div>

  <h3 class="menu-title">MASSAGES</h3>
  <svg class="menu-bracket" width="408" height="22" viewBox="0 0 408 22" aria-hidden="true">
    <path d="M1 21V1H140M268 1H407V21" fill="none" stroke="#f2b533" stroke-width="2"/>
  </svg>

  <div class="price-card price-card--one">
    <p class="price-card__name">Deep Tissue<br>Massage</p>
    <div class="price-card__rule"></div>
    <p class="price-card__time">60 minutes</p>
    <p class="price-card__price">£45</p>
    <div class="price-card__rule"></div>
    <p class="price-card__note">Oil massage personalised,<br>light to firm pressure</p>
  </div>
  <div class="price-card price-card--two">
    <p class="price-card__name">Deep Tissue<br>Massage</p>
    <div class="price-card__rule"></div>
    <p class="price-card__time">90 minutes</p>
    <p class="price-card__price">£55</p>
    <div class="price-card__rule"></div>
    <p class="price-card__note">Oil massage, medium<br>to firm pressure</p>
  </div>
  <div class="price-card price-card--three">
    <p class="price-card__name">Thai Floor Traditional<br>Massage</p>
    <div class="price-card__rule"></div>
    <p class="price-card__time">60 minutes</p>
    <p class="price-card__price">£45</p>
    <div class="price-card__rule"></div>
    <p class="price-card__note">Dry massage, medium to firm pressure<br>applying stretching technique</p>
  </div>

  <div class="photo-pair" style="top:483px">
    <div class="photo photo--left tone-warm" role="img" aria-label="Relaxed woman receiving a shoulder massage by candlelight"></div>
    <div class="photo photo--right tone-skin" role="img" aria-label="Therapist's hands massaging a client's back"></div>
  </div>

  <div class="contact">
    <p>42 Oak Row, Leeds, LS8 2BQ</p>
    <p>0113 496 0742 | www.pelinthaimassage.co.uk</p>
  </div>
</section>

</body>
</html>
```